FOOD DELIVERY BRAND NEEDS WEBSITE TO GET SUBSCRIBERS

web design needed for a food delivery brand/label,
website should display who we are, how it works and push futur clients to get the label for an online application. Should look serious/official, trustworthy and confident. colors are black and gold like logo

Target Market(s)

restaurants

Industry/Entity Type

restaurant

Number of Pages Required

4 page

Requirements
Must have
• home page, who we are, our partners, subscribe, 2 subscribe button : 1 on top 1 bottom
Nice to have
• a graphic showing average + 15% sales thanks the label

```html
<!DOCTYPE html>
<html lang="en">
<head>
<meta charset="utf-8">
<title>Aurum Plate Seal</title>
<link rel="stylesheet" href="https://fonts.googleapis.com/css2?family=Libre+Baskerville:wght@400;700&family=Poppins:wght@400;500;600&family=Oswald:wght@400;500&display=swap">
<style>
  :root {
    --gold: #d9a84a;
    --gold-dark: #b9872e;
    --black: #0b0b0b;
    --ink: #1c1c1c;
    --text: #3a3a3a;
    --hero-bg: #ebebea;
    --page-bg: #f4f4f4;
    --white: #ffffff;
    --muted: #bdbdbd;
  }
  * { box-sizing: border-box; margin: 0; padding: 0; }
  html, body { width: 1200px; height: 2397px; overflow: hidden; background: var(--page-bg); }
  body { font-family: "Poppins", sans-serif; color: var(--text); position: relative; }
  .site { position: absolute; left: 0; top: 165px; width: 1200px; height: 2068px; background: var(--white); overflow: hidden; }
  .shapes { position: absolute; left: 0; top: 0; }
  .abs { position: absolute; }

  /* header */
  .brand { position: absolute; display: flex; flex-direction: column; align-items: center; color: var(--gold); font-family: "Poppins", sans-serif; font-weight: 600; text-transform: uppercase; line-height: 1.1; text-align: center; }
  .brand-mark { width: 30px; height: 30px; border-radius: 50%; background: var(--gold); margin-bottom: 6px; }
  .brand--header { left: 200px; top: 14px; width: 103px; font-size: 11px; }
  .nav { position: absolute; left: 627px; top: 36px; display: flex; gap: 30px; font-size: 9px; font-weight: 600; color: var(--white); letter-spacing: .2px; }
  .nav .is-active { color: var(--gold); }
  .btn { position: absolute; display: flex; align-items: center; justify-content: center; background: var(--gold); color: var(--ink); font-family: "Poppins", sans-serif; font-weight: 600; font-size: 9px; text-transform: uppercase; letter-spacing: .2px; }
  .btn--outline { background: transparent; border: 1.5px solid var(--gold); color: var(--gold); }

  /* hero */
  .hero-title { left: 200px; top: 186px; width: 420px; white-space: nowrap; font-family: "Libre Baskerville", serif; font-weight: 700; font-size: 31px; line-height: 45px; color: var(--ink); }
  .badge { left: 743px; top: 462px; width: 120px; height: 120px; border-radius: 50%; background: var(--gold); border: 4px solid var(--white); box-shadow: 0 0 0 1px rgba(0,0,0,.05); display: flex; flex-direction: column; align-items: center; justify-content: center; font-family: "Oswald", sans-serif; color: var(--ink); }
  .badge::after { content: ""; position: absolute; inset: 6px; border: 1.5px dashed var(--ink); border-radius: 50%; opacity: .7; }
  .badge small { font-size: 11px; letter-spacing: .5px; }
  .badge strong { font-size: 29px; font-weight: 400; line-height: 1.15; color: var(--white); }

  /* how it works */
  .section-title { position: absolute; left: 0; width: 1200px; text-align: center; font-family: "Libre Baskerville", serif; font-weight: 700; font-size: 22px; color: var(--ink); }
  .step-label { position: absolute; width: 150px; margin-left: -75px; text-align: center; font-size: 11px; line-height: 15px; color: var(--text); }

  /* welcome */
  .welcome-kicker { left: 0; top: 1077px; width: 1200px; text-align: center; color: var(--white); font-weight: 500; font-size: 14px; }
  .welcome-title { left: 0; top: 1108px; width: 1200px; text-align: center; font-family: "Libre Baskerville", serif; font-weight: 700; font-size: 29px; color: var(--gold); }
  .welcome-copy { left: 200px; top: 1164px; width: 800px; text-align: center; color: var(--white); font-size: 9.4px; line-height: 15px; }
  .welcome-copy p + p { margin-top: 15px; }

  /* partners */
  .partner { position: absolute; top: 1497px; width: 149px; height: 80px; background: var(--white); box-shadow: 0 2px 10px rgba(0,0,0,.09); display: flex; align-items: center; justify-content: center; gap: 8px; font-family: "Poppins", sans-serif; font-weight: 600; font-size: 13px; color: var(--ink); }
  .partner i { width: 14px; height: 14px; border-radius: 50%; background: var(--gold); display: block; }
  .dots { left: 563px; top: 1607px; display: flex; gap: 9px; }
  .dots span { width: 11px; height: 11px; border-radius: 50%; border: 1.5px solid var(--gold); }
  .dots .is-active { background: var(--gold); }

  /* footer */
  .brand--footer { left: 198px; top: 1794px; width: 150px; font-size: 15px; }
  .brand--footer .brand-mark { width: 44px; height: 44px; margin-bottom: 8px; }
  .footer-heading { font-weight: 600; font-size: 12px; color: var(--gold); }
  .contact-line { display: flex; align-items: flex-start; gap: 10px; color: var(--white); font-size: 10px; line-height: 15px; }
  .contact-line svg { flex: none; margin-top: 2px; }
  .contact-line.phone { font-size: 14px; font-weight: 500; }
  .quick-links { list-style: none; color: var(--white); font-size: 9px; font-weight: 500; }
  .quick-links li { height: 22.5px; }
  .legal { top: 2000px; color: var(--white); font-size: 8.5px; font-weight: 500; }
  .legal .gold { color: var(--gold); }
  .social { position: absolute; top: 1991px; width: 30px; height: 30px; border-radius: 50%; background: #3a3a3a; }
  .social.is-active { background: var(--gold); }
</style>
</head>
<body>
<div class="site">

  <svg class="shapes" width="1200" height="2068" viewBox="0 0 1200 2068">
    <defs>
      <linearGradient id="heroGrad" x1="0" y1="0" x2="1" y2="1">
        <stop offset="0" stop-color="#f1f1f0"/>
        <stop offset="1" stop-color="#e4e4e3"/>
      </linearGradient>
      <linearGradient id="foodGrad" x1="0" y1="0" x2="1" y2="1">
        <stop offset="0" stop-color="#f3dede"/>
        <stop offset=".45" stop-color="#8a5a3e"/>
        <stop offset=".7" stop-color="#5d8a3a"/>
        <stop offset="1" stop-color="#d8744a"/>
      </linearGradient>
      <linearGradient id="welcomeGrad" x1="0" y1="0" x2="1" y2="0">
        <stop offset="0" stop-color="#2a2623"/>
        <stop offset=".55" stop-color="#1c1a19"/>
        <stop offset="1" stop-color="#3b2a24"/>
      </linearGradient>
    </defs>

    <!-- header bar -->
    <rect x="0" y="0" width="1200" height="93" fill="var(--black)"/>

    <!-- hero -->
    <polygon points="0,93 1200,93 1200,454 303,616 0,479" fill="url(#heroGrad)"/>
    <polygon points="640,93 1200,93 1200,454 760,533 580,380" fill="url(#foodGrad)" role="img" aria-label="Photo of a grilled steak with salad on a plate"/>
    <polygon points="50,490 303,662 1080,482 1000,500 303,640 85,500" fill="var(--gold)"/>

    <!-- how it works path -->
    <polyline points="203,724 280,745 440,780 600,745 760,780 920,745 995,724" fill="none" stroke="var(--gold)" stroke-width="1.2" stroke-dasharray="3 4"/>
    <circle cx="203" cy="724" r="3" fill="var(--gold)"/>
    <circle cx="995" cy="724" r="3" fill="var(--gold)"/>
    <g fill="var(--white)" stroke="var(--gold)" stroke-width="1.2" stroke-dasharray="3 3">
      <circle cx="280" cy="745" r="35"/>
      <circle cx="440" cy="780" r="35"/>
      <circle cx="600" cy="745" r="35"/>
      <circle cx="760" cy="780" r="35"/>
      <circle cx="920" cy="745" r="35"/>
    </g>
    <g fill="none" stroke="var(--gold)" stroke-width="2" stroke-linecap="round" stroke-linejoin="round">
      <path d="M266,742 a14,10 0 0 1 28,0 z M266,748 h28 M266,754 h28 v3 h-28 z"/>
      <path d="M440,796 c-9,-11 -12,-16 -12,-21 a12,12 0 0 1 24,0 c0,5 -3,10 -12,21 z"/>
      <circle cx="440" cy="775" r="4"/>
      <path d="M590,730 v12 a4,4 0 0 0 8,0 v-12 M594,730 v32 M608,730 c-5,4 -5,14 0,16 v16"/>
      <path d="M746,776 h28 l-4,16 h-20 z M752,776 l6,-10 M768,776 l-6,-10 M754,781 v7 M760,781 v7 M766,781 v7"/>
      <path d="M905,746 l7,7 l14,-14 M915,753 l14,-14"/>
    </g>

    <!-- welcome -->
    <polygon points="148,1085 898,918 1160,1082 898,940" fill="var(--gold)"/>
    <polygon points="0,1106 898,935 1200,1106 1200,1379 0,1379" fill="url(#welcomeGrad)" role="img" aria-label="Dimmed photo of a person ordering food on a laptop"/>
    <polygon points="0,1106 898,935 1200,1106 1200,1379 0,1379" fill="#000" opacity=".35"/>

    <!-- footer -->
    <path d="M123,1764 Q600,1572 1078,1764 Q600,1630 123,1764 Z" fill="var(--gold)"/>
    <path d="M0,1850 Q600,1524 1200,1850 V2068 H0 Z" fill="var(--black)"/>
    <path d="M1099,1993 l7,15 l-7,-4 l-7,4 z" fill="var(--gold)"/>
  </svg>

  <!-- header -->
  <div class="brand brand--header"><span class="brand-mark"></span>Aurum Plate<br>Seal</div>
  <nav class="nav">
    <span class="is-active">- HOME -</span>
    <span>WHO WE ARE</span>
    <span>OUR PARTNERS</span>
  </nav>
  <a class="btn" style="left:887px;top:29px;width:112px;height:36px;">Subscribe now!</a>

  <!-- hero -->
  <h1 class="abs hero-title">Lorem Ipsum is<br>simply dummy text of<br>the printing and<br>typesetting.</h1>
  <a class="btn" style="left:200px;top:387px;width:113px;height:37px;">Call now!</a>
  <div class="abs badge"><small>AVERAGE</small><strong>+ 15%</strong><small>SALES</small></div>

  <!-- how it works -->
  <h2 class="section-title" style="top:665px;">How it works</h2>
  <p class="step-label" style="left:280px;top:800px;">Open the Aurum Plate<br>and select "Food"</p>
  <p class="step-label" style="left:440px;top:831px;">Enter your delivery<br>address.</p>
  <p class="step-label" style="left:600px;top:800px;">Select your favourite<br>restaurant.</p>
  <p class="step-label" style="left:760px;top:831px;">Select a food and add<br>to your basket.</p>
  <p class="step-label" style="left:920px;top:800px;">Complete the order<br>and get ready to enjoy<br>your food.</p>

  <!-- welcome -->
  <p class="abs welcome-kicker">Welcome to</p>
  <h2 class="abs welcome-title">Aurum Plate Seal</h2>
  <div class="abs welcome-copy">
    <p>It is a long established fact that a reader will be distracted by the readable content of a page when looking at its layout. The point of using Lorem Ipsum is that it has a more-or-less normal distribution of letters, as opposed to using 'Content here, content here', making it look like readable English. Many desktop publishing packages and web page editors now use Lorem Ipsum as their default model text, and a search for 'lorem ipsum' will uncover many web sites still in their infancy.</p>
    <p>Contrary to popular belief, Lorem Ipsum is not simply random text. It has roots in a piece of classical Latin literature from 45 BC, making it over 2000 years old. Martin Hale, a Latin professor at Linden Hill College in Vermont, looked up one of the more obscure Latin words, consectetur,</p>
  </div>
  <a class="btn btn--outline" style="left:537px;top:1277px;width:124px;height:37px;">Contact us today!</a>

  <!-- partners -->
  <h2 class="section-title" style="top:1440px;">Our partners</h2>
  <div class="partner" style="left:200px;"><i></i>Ember Kitchen</div>
  <div class="partner" style="left:362px;"><i></i>Olive Table</div>
  <div class="partner" style="left:525px;"><i></i>Supper Club</div>
  <div class="partner" style="left:687px;"><i></i>Casa Verde</div>
  <div class="partner" style="left:850px;"><i></i>Bean Grove</div>
  <div class="abs dots"><span></span><span class="is-active"></span><span></span><span></span></div>

  <!-- footer -->
  <div class="brand brand--footer"><span class="brand-mark"></span>Aurum Plate<br>Seal</div>

  <div class="abs" style="left:406px;top:1793px;width:240px;">
    <h3 class="footer-heading">Contact Info</h3>
    <div class="contact-line phone" style="margin-top:14px;">
      <svg width="11" height="11" viewBox="0 0 12 12"><path d="M2,1 l3,0 l1,3 l-2,1 a7,7 0 0 0 3,3 l1,-2 l3,1 l0,3 a10,10 0 0 1 -9,-9 z" fill="var(--gold)"/></svg>123-456-7890
    </div>
    <div class="contact-line" style="margin-top:12px;">
      <svg width="11" height="9" viewBox="0 0 12 9"><rect x="0" y="0" width="12" height="9" rx="1" fill="var(--gold)"/><path d="M0.5,0.8 l5.5,4.2 l5.5,-4.2" stroke="var(--black)" fill="none"/></svg>info@aurumplate.example
    </div>
    <div class="contact-line" style="margin-top:13px;">
      <svg width="10" height="13" viewBox="0 0 10 13"><path d="M5,13 c-4,-5 -5,-7 -5,-8 a5,5 0 0 1 10,0 c0,1 -1,3 -5,8 z" fill="var(--gold)"/><circle cx="5" cy="5" r="1.8" fill="var(--black)"/></svg>Lorem House Level 3, 1500 Willis St Lorem<br>Ipsum - 6011
    </div>
  </div>

  <div class="abs" style="left:700px;top:1793px;">
    <h3 class="footer-heading">Quick Links</h3>
    <ul class="quick-links" style="margin-top:15px;">
      <li>Home</li>
      <li>Who We Are</li>
      <li>Our Partners</li>
      <li>Testimonials</li>
      <li>Contact Us</li>
    </ul>
  </div>

  <a class="btn" style="left:887px;top:1796px;width:112px;height:37px;">Subscribe now!</a>

  <p class="abs legal" style="left:200px;">© 2022 <span class="gold">Aurum Plate Seal</span>. All Right Reserved</p>
  <p class="abs legal" style="left:480px;">Terms and Conditions &nbsp;&nbsp; | &nbsp;&nbsp; Privacy Notice</p>
  <span class="social" style="left:893px;" aria-label="Social link 1"></span>
  <span class="social is-active" style="left:930px;" aria-label="Social link 2"></span>
  <span class="social" style="left:968px;" aria-label="Social link 3"></span>

</div>
</body>
</html>
```